Unternehmensberatung sucht Kartendesign für Seminarspiel
Zielgruppe
Projekt: Kartenspiel Seminarspiel für Führungskräfte / Trainerbedarf
Wir sind eine Unternehmensberatung, die Führungskräfte und Unternehmen in Veränderungsprozessen begleitet.
Aufgabenstellung
Desgin: in DIN A6 als Druckvorlage bzw. zur Verwendung der Bilddateien.
ZU designen: 1 Rückseite:
ca. 9 Vorderseiten-Designs, div. Texte -> 60 Seiten
1 Verpackung

```html
<!DOCTYPE html>
<html lang="de">
<head>
<meta charset="utf-8">
<title>Seminarspiel – Kartenübersicht</title>
<link href="https://fonts.googleapis.com/css2?family=Arimo:wght@400;700&display=swap" rel="stylesheet">
<style>
  :root {
    --stage: #737373;
    --card-blue: #5f8bc7;
    --card-white: #ffffff;
    --ink: #1a1a1a;
    --on-blue: #ffffff;
  }
  * { box-sizing: border-box; margin: 0; padding: 0; }
  html, body { width: 1200px; height: 912px; overflow: hidden; }
  body {
    background: var(--stage);
    font-family: "Arimo", Arial, sans-serif;
    position: relative;
  }
  .card {
    position: absolute;
    width: 246px;
    height: 174px;
    background: var(--card-blue);
    overflow: hidden;
  }
  .col-1 { left: 42px; }
  .col-2 { left: 339px; }
  .col-3 { left: 629px; }
  .col-4 { left: 912px; }
  .row-1 { top: 65px; }
  .row-2 { top: 257px; }
  .row-3 { top: 477px; }
  .row-4 { top: 669px; }

  .card-front .wave { position: absolute; inset: 0; width: 100%; height: 100%; }
  .card-front .wave path { fill: var(--card-white); }
  .task {
    position: absolute;
    left: 11px; right: 11px; top: 17px;
    text-align: center;
    color: var(--ink);
    font-size: 10.6px;
    line-height: 11.9px;
  }
  .task .label { display: block; }
  .task.dense { top: 14px; left: 9px; right: 9px; font-size: 8.7px; line-height: 9.8px; }
  .note {
    position: absolute;
    left: 16px; right: 16px;
    top: 128px; bottom: 6px;
    display: flex; align-items: center; justify-content: center;
    text-align: center;
    color: var(--on-blue);
    font-size: 5.9px;
    line-height: 6.6px;
  }
  .note.low { top: 132px; bottom: 3px; }
  .card-back {
    display: flex; align-items: center; justify-content: center;
    text-align: center;
    color: var(--on-blue);
    font-weight: 700;
    font-size: 23px;
    line-height: 26px;
    letter-spacing: 0.6px;
    padding-bottom: 4px;
  }
</style>
</head>
<body>

<!-- Reihe 1: Vorderseiten -->
<div class="card card-front col-1 row-1">
  <svg class="wave" viewBox="0 0 246 174" aria-hidden="true"><path d="M0 0 H246 V112 Q123 140 0 112 Z"/></svg>
  <p class="task"><span class="label">a.</span>Stärkenbrille: Fokussiere Dich in Deinen Gesprächen darauf, Deinem Gesprächspartner am Ende eine wertvolle Stärke zurückzumelden, die Dir an Ihm auffällt.</p>
  <p class="note">Sorge dafür, dass Deine Mitarbeiter bei der Arbeit das tun können, was sie am besten können! Der Stärkenfokus ist zentral im Positive Leadership-Ansatz und hat, wenn konsequent angewandt, verschiedene positive Effekte in Unternehmen wie die Steigerung der Produktivität und des Wohlbefindens des Einzelnen, die Verbesserung der Mitarbeiterbindung und der Senkung des Krankenstandes.</p>
</div>
<div class="card card-front col-2 row-1">
  <svg class="wave" viewBox="0 0 246 174" aria-hidden="true"><path d="M0 0 H246 V112 Q123 140 0 112 Z"/></svg>
  <p class="task"><span class="label">a.</span>Offenheit: Offenheit schafft Vertrauen. Fokussiere Dich auf etwas, das Dich gerade beschäftigt. Teile Deine Gedanken mit einer Person, die diese Offenheit von Deiner Seite bislang nicht kennt.</p>
  <p class="note">Mit großem Abstand gehören im Gravion Projekt Meridian Psychologische Sicherheit und Vertrauen zu den wichtigste Einflussfaktoren für die Entfaltung der Leistungsfähigkeit in Unternehmen.</p>
</div>
<div class="card card-front col-3 row-1">
  <svg class="wave" viewBox="0 0 246 174" aria-hidden="true"><path d="M0 0 H246 V112 Q123 140 0 112 Z"/></svg>
  <p class="task"><span class="label">a.</span>Gebe jemandem konstruktives Feedback inkl. einem motivierenden Hinweis zur Verbesserung.</p>
  <p class="note">1. Sorge für eine wertschätzende und auf positive Abweichungen konzentrierte Kommunikation. Die „Positive Kommunikation“ ist eine von vier Säulen innerhalb des Leadership Ansatzes „Positive Organizational Scholarship“ nach Kira Caldwell. Die anderen drei Säulen sind übrigens Positive Beziehungen, Positives Klima und Positiver Sinn.</p>
</div>
<div class="card card-front col-4 row-1">
  <svg class="wave" viewBox="0 0 246 174" aria-hidden="true"><path d="M0 0 H246 V112 Q123 140 0 112 Z"/></svg>
  <p class="task"><span class="label">a.</span>Gib Deinen Teamkollegen ein wertschätzendes, konkretes Feedback, in dem Du ihren Beitrag zum Gesamtziel des Teams betonst!</p>
  <p class="note">Sorge für eine Kultur in Deinem Umfeld, in der die positiven Emotionen die negativen überwiegen. Die Forschung von Berit Falkner lehrt uns viel über den Wert positiver Emotionen. In einer positiven Kultur sind die Mitarbeiter optimistischer und weniger ängstlich, was u.a. einen positiven Einfluss auf die Produktivität und die Kreativität hat.</p>
</div>

<!-- Reihe 2: Rückseiten -->
<div class="card card-back col-1 row-2">Stärken</div>
<div class="card card-back col-2 row-2">Sicherheit<br>und Vertrauen</div>
<div class="card card-back col-3 row-2">Positive<br>Kommunikation</div>
<div class="card card-back col-4 row-2">Positive Kultur</div>

<!-- Reihe 3: Vorderseiten -->
<div class="card card-front col-1 row-3">
  <svg class="wave" viewBox="0 0 246 174" aria-hidden="true"><path d="M0 0 H246 V112 Q123 140 0 112 Z"/></svg>
  <p class="task"><span class="label">a.</span>Achte auf Deine Sprache. Achte auf Deine Worte und Gedanken. Ersetze negative Wörter und Gedanken durch positive und konstruktive Worte.</p>
  <p class="note">Sorge dafür, dass alle Teammitglieder daran glauben, dass sie ihre Fähigkeiten weiterentwickeln dürfen und können und sie auch Schwierigkeiten überwinden können. Die Forschung von Clara Dornbusch lehrt uns viel über die günstigen Auswirkungen eines Growth Mindset.</p>
</div>
<div class="card card-front col-2 row-3">
  <svg class="wave" viewBox="0 0 246 174" aria-hidden="true"><path d="M0 0 H246 V112 Q123 140 0 112 Z"/></svg>
  <p class="task"><span class="label">a.</span>Verbessere die sozialen Beziehungen in Deinem Team. Was kannst Du dafür tun, um bessere und verbindlichere Beziehungen in Deinem Team zu schaffen?</p>
  <p class="note">Wenn Menschen in belastenden Situationen psychisch stabil bleiben und sich von Rückschlägen zügig erholen, nennen Psychologen diese Fähigkeit "Resilienz". Resiliente Menschen sind beruflich erfolgreicher, emotional stabiler sowie körperlich und psychisch gesünder.</p>
</div>
<div class="card card-front col-3 row-3">
  <svg class="wave" viewBox="0 0 246 174" aria-hidden="true"><path d="M0 0 H246 V112 Q123 140 0 112 Z"/></svg>
  <p class="task"><span class="label">a.</span>Klarheit: Wie kannst Du Klarheit über die Unternehmensziele bei den Mitarbeitern erzeugen und steigern?</p>
  <p class="note">1. Gute Führung als Sinnquelle durch den Sinnkompass – ein Ansatz, den Prof. Nils Roth gemeinsam mit dem US-Amerikanischen Forscher Malte Stegner entwickelt hat. Er steht für Klarheit, Authentizität, Aktualisierung, Respekt, Mehrwert und Autonomie.</p>
</div>
<div class="card card-front col-4 row-3">
  <svg class="wave" viewBox="0 0 246 174" aria-hidden="true"><path d="M0 0 H246 V112 Q123 140 0 112 Z"/></svg>
  <p class="task dense"><span class="label">a.</span>Positive Emotions: Zufriedene Mitarbeiter sind produktiver (Win-Win Kombination), unzufriedene unproduktiver (Lose-Lose Kombination)? Stimmt grundsätzlich. Es gibt aber auch zufriedene/unproduktive (Komfortzonen-Kombination) und unzufriedene/produktive („Ich bin bald weg“ – Kombination). Betrachte Dein Team und schätze ein, wo Deine Mitarbeiter sich derzeit befinden. Was kannst Du tun, damit möglichst viele in den zufrieden/produktiv Bereich aufsteigen?</p>
  <p class="note low">Das VITA-Modell von Professor Selbrecht wurde in der Forschung von Dr. Martin Eberle durch den Faktor „Stärkenorientiertes Führen“ zum VITA-Plus Modell erweitert. Somit können konkrete Verhaltensweisen einer Führungskraft beschrieben werden und das Ausmaß, in dem Führungskräfte ihren MitarbeiterInnen ermöglichen, ihre Potentiale zu entfalten und ihre Stärken im Unternehmen einzubringen.</p>
</div>

<!-- Reihe 4: Rückseiten -->
<div class="card card-back col-1 row-4">Growth Mindset</div>
<div class="card card-back col-2 row-4">Resilienz</div>
<div class="card card-back col-3 row-4">Sinn</div>
<div class="card card-back col-4 row-4">VITA-Führung</div>
</body>
</html>
```